Copper Lane Assembly Lanterns EP Design Cover

I need a CD cover design for my EP titled "Lanterns". The theme can be either the alphabetic letters, or written letters, whichever seems best for your graphic concept.<br/><br/>Please take a listen to the tracks on tunebasin here:<br/>https://tunebasin.example/copper-lane-assembly<br/>And here:<br/>https://tunebasin.example/copper-lane-assembly/silver-morning/s-KQ7rT<br/>https://tunebasin.example/copper-lane-assembly/rain-on-the-porch-demo-mix/s-WM4PZ<br/><br/>I look forward to seeing you designs and choosing one for the EP cover.

Target Market(s)

Indie-pop/rock

Colors

Designer to choose colors to be used in the design.

Requirements
Must have
• Copper Lane Assembly Logo
• Should meet Friendloop criteria for % text to picture ratio

```html
<!DOCTYPE html>
<html lang="en">
<head>
<meta charset="utf-8">
<title>Lanterns — Copper Lane Assembly</title>
<link href="https://fonts.googleapis.com/css2?family=Bebas+Neue&family=Big+Shoulders+Display:wght@300&display=swap" rel="stylesheet">
<style>
  :root {
    --paper-light: #f1f0eb;
    --paper-edge: #c4c5bf;
    --type-dark: #3d3834;
    --type-mid: #6e685f;
    --type-light: #9b968c;
    --logo-box: #1c0f0d;
    --logo-ink: #f4f1ec;
    --tray-steel: #9a998f;
    --tray-grey: #7d7b72;
    --tray-rust: #86654e;
    --tray-shadow: #5a554d;
    --shelf-rail: #6b4a37;
  }
  html, body {
    margin: 0;
    padding: 0;
    width: 1200px;
    height: 1200px;
    overflow: hidden;
  }
  .cover {
    position: relative;
    width: 1200px;
    height: 1200px;
    background: radial-gradient(ellipse at 50% 45%, var(--paper-light) 45%, var(--paper-edge) 100%);
  }
  .cover svg {
    display: block;
    width: 1200px;
    height: 1200px;
  }
  .title {
    font-family: "Bebas Neue", "Oswald", sans-serif;
    font-size: 408px;
    text-transform: uppercase;
  }
  .band-name {
    font-family: "Big Shoulders Display", "Antonio", sans-serif;
    font-weight: 300;
    fill: var(--logo-ink);
    text-transform: uppercase;
  }
  .shelf-rail {
    fill: var(--shelf-rail);
    opacity: 0.85;
  }
</style>
</head>
<body>
<main class="cover">
  <svg viewBox="0 0 1200 1200" xmlns="http://www.w3.org/2000/svg">
    <defs>
      <linearGradient id="weathered-metal" x1="0" y1="0" x2="1" y2="0.4">
        <stop offset="0" stop-color="var(--type-dark)"/>
        <stop offset="0.35" stop-color="var(--type-mid)"/>
        <stop offset="0.6" stop-color="var(--type-dark)"/>
        <stop offset="1" stop-color="var(--type-light)"/>
      </linearGradient>
      <linearGradient id="type-tray" x1="0" y1="0" x2="1" y2="1">
        <stop offset="0" stop-color="var(--tray-grey)"/>
        <stop offset="0.35" stop-color="var(--tray-steel)"/>
        <stop offset="0.55" stop-color="var(--tray-shadow)"/>
        <stop offset="0.72" stop-color="var(--tray-rust)"/>
        <stop offset="1" stop-color="var(--tray-steel)"/>
      </linearGradient>
    </defs>

    <text class="title" x="98" y="378" textLength="1036" lengthAdjust="spacingAndGlyphs" fill="url(#weathered-metal)">Lanterns</text>

    <rect class="type-tray" x="94" y="412" width="1030" height="788" fill="url(#type-tray)" role="img" aria-label="Photograph of rows of worn metal letterpress type in a wooden tray"/>

    <g class="tray-shelves" aria-hidden="true">
      <rect class="shelf-rail" x="542" y="562" width="582" height="5"/>
      <rect class="shelf-rail" x="542" y="742" width="582" height="5"/>
      <rect class="shelf-rail" x="94" y="912" width="1030" height="5"/>
      <rect class="shelf-rail" x="94" y="1086" width="1030" height="5"/>
    </g>

    <g class="band-logo">
      <rect x="94" y="412" width="448" height="448" fill="var(--logo-box)"/>
      <text class="band-name" x="200" y="572" font-size="167" textLength="240" lengthAdjust="spacingAndGlyphs">Copper</text>
      <text class="band-name" x="200" y="714" font-size="147" textLength="240" lengthAdjust="spacingAndGlyphs">Lane</text>
      <text class="band-name" x="200" y="818" font-size="100" textLength="240" lengthAdjust="spacingAndGlyphs">Assembly</text>
    </g>
  </svg>
</main>
</body>
</html>
```